Oral Surgeon Referral Pads

Hello. We need referral pads for Dr Helena Vasquier, DDS board certified oral surgeon's new office - Cedar Hollow Oral & Maxillofacial Surgery. See logo uploaded. See some images we would like included
Updates

Designs look the same

Font styles to use
Serif
Script

Colors
00AB8E
00BBA5
67D7C9
C6EFE9
E9F9F6

Requirements
Must have
• Color Pantone 623c. Also foldable business cards

```html
<!DOCTYPE html>
<html lang="en">
<head>
<meta charset="utf-8">
<title>Cedar Hollow Oral &amp; Maxillofacial Surgery — Stationery</title>
<link href="https://fonts.googleapis.com/css2?family=Tinos:wght@400;700&family=Arimo&family=Open+Sans&display=swap" rel="stylesheet">
<style>
  :root{
    --backdrop:#d1d1d1;
    --paper:#ffffff;
    --sage:#9dbab0;
    --sage-text:#8fb1a6;
    --rule-dark:#5e5e5e;
    --ink:#4a4a4a;
    --ink-soft:#5a5a5a;
    --shadow:0 3px 6px rgba(0,0,0,.35);
  }
  *{box-sizing:border-box;margin:0;padding:0}
  html,body{width:1200px;height:1055px;overflow:hidden;background:var(--backdrop)}
  body{position:relative;font-family:"Tinos",serif;color:var(--ink)}

  .sheet{position:absolute;background:var(--paper);box-shadow:var(--shadow)}

  /* Letterhead */
  .letterhead{left:53px;top:122px;width:573px;height:811px}
  .contact-list{position:absolute;list-style:none;font-size:9px;line-height:12px;color:var(--ink-soft)}
  .contact-list li{display:flex;align-items:center;gap:5px}
  .contact-list svg{width:7px;height:7px;fill:none;stroke:var(--sage);stroke-width:1.4}
  .letterhead .contact-list{left:37px;top:44px}
  .letterhead .address{position:absolute;right:38px;top:49px;text-align:right;font-size:9px;line-height:12px;color:var(--ink-soft)}

  .brand{position:absolute;left:0;right:0;text-align:center;color:var(--sage-text);font-family:"Tinos",serif;font-weight:400}
  .brand .brand-name{display:block}
  .letterhead .brand{top:58px}
  .letterhead .brand-name{font-size:19px;line-height:22px}

  .band{position:absolute;left:0;right:0;display:flex;align-items:center}
  .band .bar{flex:1;height:7px;background:var(--sage)}
  .band .band-label{padding:0 4px;color:var(--sage-text);font-family:"Tinos",serif}
  .rule{position:absolute;left:0;right:0;height:2px;background:var(--rule-dark)}
  .letterhead .band{top:90px}
  .letterhead .band-label{font-size:10px}
  .letterhead .rule{top:107px}

  .letter{position:absolute;left:52px;top:250px;width:472px;font-family:"Arimo",sans-serif;color:var(--ink)}
  .letter .salutation{font-family:"Open Sans",sans-serif;font-size:11.5px;margin-bottom:20px}
  .letter p{font-size:9.1px;line-height:11.8px;margin-bottom:10.5px}
  .letter .closing{font-family:"Open Sans",sans-serif;font-size:6px;margin-top:20px}

  /* Business card front */
  .card-front{left:662px;top:334px;width:485px;height:276px;background:var(--sage)}
  .card-front .brand{top:96px;color:#ffffff}
  .card-front .brand-name{font-size:30px;line-height:34px}
  .card-front .brand-sub{font-size:16px;line-height:22px;display:block}

  /* Business card back */
  .card-back{left:662px;top:656px;width:485px;height:277px}
  .card-back .brand{top:80px}
  .card-back .brand-name{font-size:22px;line-height:24px}
  .card-back .band{top:113px}
  .card-back .band-label{font-size:12px}
  .card-back .rule{top:134px}
  .person{position:absolute;right:255px;top:172px;text-align:right}
  .person .name{font-family:"Tinos",serif;font-weight:700;font-size:16px;letter-spacing:.3px;color:var(--sage-text);text-transform:uppercase}
  .person .role{font-size:12px;color:var(--ink-soft);line-height:16px}
  .divider{position:absolute;left:242px;top:169px;width:1px;height:43px;background:var(--rule-dark)}
  .card-back .contact-list{left:254px;top:164px;font-size:12.5px;line-height:17.5px}
  .card-back .contact-list svg{width:10px;height:10px}
  .card-back .contact-list li{gap:6px}
  .card-back .address{position:absolute;left:0;right:0;top:240px;text-align:center;font-size:12.5px;color:var(--ink-soft)}
</style>
</head>
<body>

<section class="sheet letterhead">
  <ul class="contact-list">
    <li><svg viewBox="0 0 10 10"><path d="M2 1l2 2-1 1.5c.8 1.5 1.5 2.2 3 3L7.5 6l2 2-1.5 1.5C4 9 1 6 .5 1.5z"/></svg>123-456-2100</li>
    <li><svg viewBox="0 0 10 10"><rect x="1" y="2" width="8" height="6"/><path d="M1 2l4 3.5L9 2"/></svg>youremail@gmail.com</li>
    <li><svg viewBox="0 0 10 10"><circle cx="5" cy="5" r="4"/><path d="M1 5h8M5 1c2 2 2 6 0 8M5 1c-2 2-2 6 0 8"/></svg>www.yourwebsite.com</li>
  </ul>

  <div class="brand"><span class="brand-name">Cedar Hollow</span></div>
  <div class="band"><span class="bar"></span><span class="band-label">Oral &amp; Maxillofacial Surgery</span><span class="bar"></span></div>
  <div class="rule"></div>

  <address class="address" style="font-style:normal">Your address<br>city<br>state, ZIP 0000</address>

  <article class="letter">
    <p class="salutation">Dear Mr. Smith,</p>
    <p>Lorem ipsum dolor sit amet, consectetuer adipiscing elit, sed diam nonmmy nibh euismod tincidunt ut laor eet dolore magna aliquam erat volutpat. Ut wisi enim ad minim veniam, quis nostrud exerci tationmcorper suscipit lobortis nisl ut aliquip ex ea commodo consequat. Duis autem vel eum iriure dolor in hendrerit in vulputate velit esse molestie consequat, vel illum dolore eu feugiat</p>
    <p>Rorem ipsum dolor sit amet, consectetuer adipiscing elit, sed diam nonmmy nibh euismod tincidunt ut laor eet dolore magna aliquam erat volutpat. Ut wisi enim ad minim veniam, quis nostrud exerci tationmcorper suscipit lobortis nisl ut aliquip ex ea commodo consequat. Duis autem vel eum iriure dolor in hendrerit in vulputate velit esse molest</p>
    <p>Dorem ipsum dolor sit amet, consectetuer adipiscing elit, sed diam nonmmy nibh euismod tincidunt ut laor eet dolore magna aliquam erat volutpat. Ut wisi enim ad minim veniam, quis nostrud exerci tationmcorper suscipit lobortis nisl ut aliquip ex ea commodo consequat. Duis autem vel eum iriure dolor in hendrerit in suscipit lobortis nisl ut aliquip ex ea commodo consequat. Duis autem vel eum iriure dolor in hendrerit in vulputate velit esse molestie consequat, vel illum</p>
    <p>Sorem ipsum dolor sit amet, consectetuer adipiscing elit, sed diam nonmmy nibh euismod tincidunt ut laor eet dolore magna aliquam erat volutpat. Ut wisi enim ad minim veniam, quis nostrud exerci tationmcorper suscipit lobortis nisl ut aliquip ex ea commodo consequat. Duis autem vel eum iriure dolor in</p>
    <p class="closing">Sincerely,</p>
  </article>
</section>

<section class="sheet card-front">
  <div class="brand">
    <span class="brand-name">Cedar Hollow</span>
    <span class="brand-sub">Oral &amp; Maxillofacial Surgery</span>
  </div>
</section>

<section class="sheet card-back">
  <div class="brand"><span class="brand-name">Cedar Hollow</span></div>
  <div class="band"><span class="bar"></span><span class="band-label">Oral &amp; Maxillofacial Surgery</span><span class="bar"></span></div>
  <div class="rule"></div>

  <div class="person">
    <div class="name">Jonathan Smith</div>
    <div class="role">Manager</div>
  </div>
  <div class="divider"></div>
  <ul class="contact-list">
    <li><svg viewBox="0 0 10 10"><path d="M2 1l2 2-1 1.5c.8 1.5 1.5 2.2 3 3L7.5 6l2 2-1.5 1.5C4 9 1 6 .5 1.5z"/></svg>123-456-2100</li>
    <li><svg viewBox="0 0 10 10"><rect x="1" y="2" width="8" height="6"/><path d="M1 2l4 3.5L9 2"/></svg>youremail@gmail.com</li>
    <li><svg viewBox="0 0 10 10"><circle cx="5" cy="5" r="4"/><path d="M1 5h8M5 1c2 2 2 6 0 8M5 1c-2 2-2 6 0 8"/></svg>www.yourwebsite.com</li>
  </ul>
  <div class="address">Your Address, City, State, Zip 0000</div>
</section>

</body>
</html>
```